BOLD & MINIMALIST DESIGN NEEDED

We want a very bold but minimalistic business card design that is impactful and utilizes both sides of the business card. Our current logo is included for your use.

We want bold fonts and good use of negative space. We don't want the logo to overpower the design.

Target Market(s)

Professionals who are building new commercial buildings.

Industry/Entity Type

Construction

Contact Information for Business Card

Name, Title, email, office phone, cell phone, website

Font styles to use
Serif
Sans Serif

Requirements
Must have
• Bold design!

```html
<!DOCTYPE html>
<html lang="en">
<head>
<meta charset="utf-8">
<title>Kestrel Design + Build — Business Card</title>
<link href="https://fonts.googleapis.com/css2?family=Arimo:wght@400;700&display=swap" rel="stylesheet">
<style>
  :root {
    --page-bg: #e4e4e4;
    --card-white: #ffffff;
    --ink: #111111;
    --text-grey: #555555;
    --brand-green: #8cc63f;
    --green-light: #b8de82;
    --green-dark: #86c22f;
  }
  * { margin: 0; padding: 0; box-sizing: border-box; }
  html, body {
    width: 1200px; height: 1200px; overflow: hidden;
    background: var(--page-bg);
    font-family: "Arimo", Arial, sans-serif;
  }
  .card {
    position: absolute;
    left: 255px;
    width: 690px;
    height: 394px;
  }
  .card-front { top: 150px; background: var(--card-white); }
  .card-back {
    top: 656px;
    background: radial-gradient(ellipse at 50% 40%, var(--green-light) 0%, var(--brand-green) 60%, var(--green-dark) 100%);
    display: flex; align-items: center; justify-content: center;
  }
  .person-name {
    position: absolute; left: 40px; top: 54px;
    font-size: 27px; font-weight: 700; color: var(--ink); letter-spacing: 0.5px;
  }
  .person-title {
    position: absolute; left: 40px; top: 86px;
    font-size: 16px; color: var(--brand-green);
  }
  .corner-name {
    position: absolute; right: 40px; top: 60px;
    font-size: 18px; font-weight: 700; color: var(--ink);
    display: flex; align-items: center; gap: 8px;
  }
  .corner-name .mark { width: 14px; height: 14px; background: var(--brand-green); }
  .company-name {
    position: absolute; left: 40px; top: 230px;
    font-size: 30px; font-weight: 700; color: var(--ink); letter-spacing: 0.5px;
  }
  .contact {
    position: absolute; left: 40px; top: 312px;
    font-size: 16px; line-height: 21px; color: var(--text-grey);
  }
  .contact .label { color: var(--brand-green); font-weight: 700; }
  .contact .divider { margin: 0 10px; }
  .back-name {
    font-size: 50px; font-weight: 700; color: var(--ink); letter-spacing: 1px;
  }
</style>
</head>
<body>
  <section class="card card-front">
    <div class="person-name">MARCUS HALE</div>
    <div class="person-title">President</div>
    <div class="corner-name"><span class="mark"></span>KESTREL</div>
    <div class="company-name">KESTREL DESIGN + BUILD</div>
    <div class="contact">
      <div><span class="label">P :</span> 555-210-4187 <span class="label">C :</span> 555-384-9026</div>
      <div>info@kestrelbuild.com<span class="divider">|</span>www.kestrelbuild.com</div>
    </div>
  </section>
  <section class="card card-back">
    <div class="back-name">KESTREL DESIGN + BUILD</div>
  </section>
</body>
</html>
```